Maple Lantern Business Card

Design of business cards

Target Market(s)

We are aiming as small business owners who need anything from basic business structures, website plans, business processes and quality assurance.

Industry/Entity Type

Business

Colors

Designer to choose colors to be used in the design.

Requirements
Nice to have
• I would prefer one side of the card to use the green from the logo. Prefer to have the same font as the logo.

```html
<!DOCTYPE html>
<html lang="en">
<head>
<meta charset="utf-8">
<title>Maple Lantern Consulting – Business Card</title>
<link rel="stylesheet" href="https://fonts.googleapis.com/css2?family=Cinzel:wght@500&family=Crimson+Text:wght@400;700&display=swap">
<style>
  :root {
    --bg: #e9e9e9;
    --green: #a3cb2b;
    --green-soft: #b3d54a;
    --white: #ffffff;
    --charcoal: #454547;
    --ink: #1f1f1f;
    --wordmark-light: #eef5d4;
  }
  * { box-sizing: border-box; margin: 0; padding: 0; }
  html, body { width: 1200px; height: 1200px; overflow: hidden; }
  body {
    background: var(--bg);
    position: relative;
    font-family: "Crimson Text", Georgia, serif;
  }
  .card {
    position: absolute;
    left: 180px;
    width: 840px;
    height: 480px;
    overflow: hidden;
    box-shadow: 0 6px 18px rgba(0,0,0,0.12);
  }
  .card--front { top: 90px; background: var(--white); }
  .card--back { top: 630px; background: var(--charcoal); }

  /* Front */
  .front__band {
    position: absolute; left: 0; width: 100%;
    background: linear-gradient(135deg, var(--green) 0%, var(--green-soft) 50%, var(--green) 100%);
  }
  .front__band--top { top: 0; height: 104px; }
  .front__band--bottom { top: 262px; bottom: 0; }
  .front__brand {
    position: absolute; left: 130px; top: 130px;
    display: flex; align-items: center; gap: 26px;
  }
  .brand-dot {
    width: 78px; height: 78px; border-radius: 50%;
    background: var(--green);
    flex: none;
  }
  .wordmark {
    font-family: "Cinzel", "Times New Roman", serif;
    font-weight: 500;
    font-size: 30px;
    line-height: 1.08;
    letter-spacing: 1px;
    color: var(--green);
  }

  /* Back */
  .back__band {
    position: absolute; left: 0; top: 150px; width: 100%; height: 170px;
    background: var(--green);
    display: flex; align-items: center;
    padding: 0 60px;
  }
  .back__brand { display: flex; align-items: center; gap: 22px; }
  .back__brand .brand-dot { width: 70px; height: 70px; background: var(--wordmark-light); }
  .back__brand .wordmark { color: var(--wordmark-light); font-size: 27px; }
  .divider {
    width: 2px; height: 84px; background: var(--ink);
    margin: 0 28px 0 40px;
  }
  .contact { color: var(--ink); }
  .contact__name { font-weight: 700; font-size: 26px; }
  .contact__phone {
    display: flex; align-items: center; gap: 8px;
    font-size: 19px; margin-top: 2px;
  }
  .contact__phone svg { width: 20px; height: 20px; }
</style>
</head>
<body>
  <section class="card card--front" aria-label="Card front">
    <div class="front__band front__band--top" role="img" aria-label="Repeating green monogram pattern"></div>
    <div class="front__brand">
      <span class="brand-dot"></span>
      <div class="wordmark">Maple<br>Lantern<br>Consulting</div>
    </div>
    <div class="front__band front__band--bottom" role="img" aria-label="Repeating green monogram pattern"></div>
  </section>

  <section class="card card--back" aria-label="Card back">
    <div class="back__band">
      <div class="back__brand">
        <span class="brand-dot"></span>
        <div class="wordmark">Maple<br>Lantern<br>Consulting</div>
      </div>
      <span class="divider"></span>
      <div class="contact">
        <p class="contact__name">Name : xxxx xxx</p>
        <p class="contact__phone">
          <svg viewBox="0 0 20 20" aria-hidden="true">
            <circle cx="10" cy="10" r="9" fill="#1f1f1f"/>
            <path d="M7 5.5c.6 0 1 .3 1.2.8l.6 1.4c.2.4 0 .9-.3 1.1l-.6.4c.5 1.1 1.4 2 2.5 2.5l.4-.6c.3-.4.7-.5 1.1-.3l1.4.6c.5.2.8.7.7 1.2-.2 1.1-1.1 1.9-2.2 1.9C8.5 14.5 5.5 11.5 5.5 8c0-1.3.7-2.3 1.5-2.5z" fill="#a3cb2b"/>
          </svg>
          xxx xxx-xxxx
        </p>
      </div>
    </div>
  </section>
</body>
</html>
```